Talvora Health Artificial Intelligence MedTech Software Website Refresh

We need a new website (old one at www.talvora-health.example is no longer relevant) for our medtech software company using artificial intelligence to deliver higher quality, faster and more cost effective care in oncology. The audiences are both healthcare providers and health insurance payers. We've created an extensive outline to follow and have the old site still live for easy content use and repurposing. Our primary need is a great overhaul to look and feel. If we find a successful designer, we will need additional work done for graphics and other presentation projects.

Target Market(s)

Health care providers (doctors) and administrators plus health insurers

Industry/Entity Type

Medtech

Number of Pages Required

5+ page

Font styles to use
Other font styles liked:
• Roboto see Style Guide

Requirements
Must have
• See attached brief
Nice to have
• See attached brief. We like www.carenix.example and www.plumotech.example as sites.
Should not have
• See attached brief

```html
<!DOCTYPE html>
<html lang="en">
<head>
<meta charset="utf-8">
<title>Talvora Health</title>
<link href="https://fonts.googleapis.com/css2?family=Roboto:wght@400;500;700;900&display=swap" rel="stylesheet">
<style>
:root{
  --blue-deep:#1b6cc2;
  --blue:#1a75c9;
  --blue-light:#33b1e6;
  --navy:#383d4f;
  --ink:#1c1c1c;
  --muted:#7a7a7a;
  --grey-bg:#f4f4f4;
  --white:#ffffff;
  --footer:#1b7fd3;
}
*{margin:0;padding:0;box-sizing:border-box}
html,body{width:1200px;height:3153px;overflow:hidden}
body{position:relative;font-family:"Roboto",sans-serif;background:var(--white);color:var(--ink)}
.abs{position:absolute}
.backdrop{position:absolute;left:0;top:0;width:1200px;height:3153px}
.brand{display:flex;align-items:center;gap:12px;color:var(--white);font-weight:700;font-size:34px;letter-spacing:.5px}
.brand .dot{width:18px;height:18px;border-radius:50%;background:var(--blue-light)}
.nav{left:640px;top:60px;display:flex;gap:27px;font-size:15px;font-weight:500;color:var(--white)}
.nav .active{color:#5fd0f5;border-bottom:2px solid #5fd0f5;padding-bottom:6px}
.hero-title{left:110px;top:196px;font-size:50px;font-weight:700;color:var(--white);letter-spacing:.3px}
.hero-lead{left:110px;top:266px;width:500px;font-size:15.5px;font-weight:500;line-height:24px;color:var(--white)}
.hero-points{left:110px;top:354px;width:500px;list-style:none;color:var(--white);font-size:13.5px;line-height:21.5px}
.hero-points li{position:relative;padding-left:26px;margin-bottom:15px}
.hero-points li::before{content:"";position:absolute;left:0;top:5px;width:12px;height:12px;border-radius:50%;background:var(--white)}
.hero-points li::after{content:"";position:absolute;left:3px;top:8px;width:5px;height:3px;border-left:2px solid var(--blue);border-bottom:2px solid var(--blue);transform:rotate(-45deg)}
.photo{position:absolute;width:140px;height:140px;border-radius:50%;background:radial-gradient(circle at 40% 35%,#e8e3de,#a9a9ab);border:3px solid rgba(255,255,255,.6)}
.section-title{left:0;width:1200px;text-align:center;font-size:37px;font-weight:700;color:var(--ink)}
.section-title span{color:var(--blue)}
.intro{left:190px;top:884px;width:820px;text-align:center;font-size:14px;line-height:25.7px;color:var(--muted)}
.stat{position:absolute;border-radius:50%;display:flex;flex-direction:column;align-items:center;justify-content:center;color:var(--white);text-align:center}
.stat.dark{width:310px;height:310px;background:var(--navy)}
.stat.main{width:342px;height:342px;background:linear-gradient(180deg,#45c3ee,#1577cf);box-shadow:0 0 0 14px var(--white),0 4px 24px 14px rgba(0,0,0,.08)}
.stat .fig{font-size:39px;font-weight:900;line-height:43px;margin-top:14px}
.stat .who{font-size:24px;font-weight:500;margin-top:14px}
.stat.main .fig{font-size:39px}
.stat.main .who{font-size:23px;line-height:28px;margin-top:14px}
.feature{position:absolute;top:1462px;width:240px;text-align:center}
.feature .icon{width:100px;height:100px;border-radius:50%;background:#eef0f3;margin:0 auto;display:flex;align-items:center;justify-content:center}
.feature h3{font-size:17px;font-weight:500;margin-top:18px;color:var(--ink)}
.feature p{font-size:13.5px;line-height:21.5px;color:var(--muted);margin-top:10px}
.card{position:absolute;top:1951px;width:314px;height:363px;background:var(--white);border:1px solid #dcdcdc}
.card .thumb{height:206px;background:linear-gradient(135deg,#2f78b9,#a7c8e0)}
.card h4{font-size:16.5px;font-weight:500;line-height:22px;margin:22px 22px 0 23px;color:var(--ink)}
.card .meta{font-size:13px;color:#9a9a9a;margin:10px 0 0 23px}
.card .rule{height:1px;background:#e4e4e4;margin:12px 22px 0 22px}
.card .dl{font-size:14.5px;color:var(--blue);font-weight:500;margin:14px 0 0 23px;display:flex;align-items:center;gap:8px}
.scroll{left:1127px;top:1951px;width:13px;height:362px;background:#e6e6e6}
.scroll i{position:absolute;left:2px;top:14px;width:9px;height:126px;background:#c9cfd8}
.partner{position:absolute;top:2604px;width:237px;height:112px;background:var(--white);box-shadow:0 2px 10px rgba(0,0,0,.07);display:flex;align-items:center;justify-content:center;text-align:center;font-size:21px;font-weight:500;color:#6d6d6d;line-height:24px;padding:0 18px}
.footer-col h5{font-size:16px;font-weight:500;color:var(--white);margin-bottom:18px}
.footer-col a{display:block;color:var(--white);font-size:13.5px;text-decoration:none;line-height:25.7px}
.social{position:absolute;top:3001px;width:38px;height:38px;border-radius:50%;border:2px solid var(--white)}
.copy{left:0;width:1200px;top:3116px;text-align:center;font-size:15px;color:var(--white)}
</style>
</head>
<body>
<svg class="backdrop" viewBox="0 0 1200 3153" aria-hidden="true">
  <defs>
    <linearGradient id="heroGrad" x1="0" y1="0" x2="1" y2="0.3">
      <stop offset="0" stop-color="#1d6cc3"/>
      <stop offset="1" stop-color="#33aee3"/>
    </linearGradient>
  </defs>
  <path d="M0 0H1200V637Q600 810 0 625Z" fill="url(#heroGrad)"/>
  <path d="M0 1727Q600 1897 1200 1727V2486Q600 2326 0 2486Z" fill="#f4f4f4"/>
  <rect x="0" y="2804" width="1200" height="349" fill="#1b7fd3"/>
  <line x1="465" y1="2872" x2="465" y2="3104" stroke="rgba(255,255,255,.25)"/>
  <line x1="817" y1="2872" x2="817" y2="3104" stroke="rgba(255,255,255,.25)"/>
  <line x1="110" y1="3107" x2="1090" y2="3107" stroke="rgba(255,255,255,.25)"/>
  <path d="M62 2648L50 2661L62 2674" fill="none" stroke="#222" stroke-width="2"/>
  <path d="M1138 2648L1150 2661L1138 2674" fill="none" stroke="#222" stroke-width="2"/>
</svg>

<header>
  <div class="abs brand" style="left:110px;top:48px"><span>Talvora Health</span><span class="dot"></span></div>
  <nav class="abs nav">
    <span class="active">Home</span><span>Solutions</span><span>Clinical Evidence</span><span>About</span><span>Contact Us</span>
  </nav>
</header>

<section class="hero">
  <h1 class="abs hero-title">TALVORA HEALTH, INC.</h1>
  <p class="abs hero-lead">Talvora Health, Inc. is an expert team with the vision of improving oncology treatment delivery, patient outcomes and cost effectiveness through the power of AI.</p>
  <ul class="abs hero-points">
    <li>The problem(s) for providers: creating a treatment directive starts from scratch for every patient and is a time consuming iterative/back and forth process . Further, because there is little transparency to communicate patient-specific treatment needs to the payer, prior authorization is a burden.</li>
    <li>The problem for payers: there is no transparency to the uniqueness of the patient<br>so the process has costly delays to gather more information and align the treatment to what's best for the patient; often attempts to redirect care are</li>
  </ul>
  <div class="photo" style="left:834px;top:136px" role="img" aria-label="Portrait photo of a patient in a headscarf"></div>
  <div class="photo" style="left:667px;top:303px" role="img" aria-label="Photo of a hand holding a syringe"></div>
  <div class="photo" style="left:834px;top:303px" role="img" aria-label="Photo of a patient's shoulder"></div>
  <div class="photo" style="left:1001px;top:303px" role="img" aria-label="Photo of a clinic room"></div>
  <div class="photo" style="left:834px;top:471px" role="img" aria-label="Photo of hands applying a bandage"></div>
</section>

<section class="solutions">
  <h2 class="abs section-title" style="top:811px">OUR <span>SOLUTIONS</span></h2>
  <p class="abs intro">Talvora Health improves cancer therapy through AI-powered analysis and comparison of over 10 million clinical images and over 30,000 patient datasets.Our commercially available, FDA-cleared software suite uses AI to match each new patient to a massive, proprietary, expert database in order to precisely tailor treatment to each patient's unique characteristics, and align the treatment directive between the payer and provider to what's best for the patient.</p>

  <div class="stat dark" style="left:145px;top:1067px">
    <svg width="76" height="66" viewBox="0 0 76 66" fill="none" stroke="#fff" stroke-width="3"><rect x="4" y="40" width="9" height="22"/><rect x="22" y="32" width="9" height="30"/><rect x="40" y="38" width="9" height="24"/><rect x="58" y="22" width="9" height="40"/><polyline points="8,28 26,18 44,24 62,6"/><circle cx="8" cy="28" r="3"/><circle cx="26" cy="18" r="3"/><circle cx="44" cy="24" r="3"/><circle cx="62" cy="6" r="3"/></svg>
    <div class="fig">$15M<br>PMPY</div><div class="who">Payer</div>
  </div>
  <div class="stat main" style="left:429px;top:1051px">
    <svg width="80" height="70" viewBox="0 0 80 70" fill="none" stroke="#fff" stroke-width="3"><rect x="4" y="14" width="10" height="48"/><rect x="22" y="26" width="10" height="36"/><rect x="40" y="38" width="10" height="24"/><rect x="58" y="46" width="10" height="16"/><line x1="0" y1="66" x2="76" y2="66"/><path d="M6 4Q40 6 66 22"/><polyline points="58,20 68,23 64,13"/></svg>
    <div class="fig">Patient</div><div class="who">30% reduction in<br>side efforts</div>
  </div>
  <div class="stat dark" style="left:744px;top:1067px">
    <svg width="76" height="76" viewBox="0 0 76 76" fill="none" stroke="#fff" stroke-width="3"><circle cx="30" cy="18" r="13"/><path d="M6 74V56Q6 40 30 40Q54 40 54 56"/><rect x="46" y="56" width="7" height="18"/><rect x="58" y="46" width="7" height="28"/><rect x="34" y="62" width="7" height="12"/></svg>
    <div class="fig">$4k/<br>Patient</div><div class="who">Provider</div>
  </div>

  <div class="feature" style="left:78px">
    <div class="icon"><svg width="52" height="52" viewBox="0 0 52 52" fill="none" stroke="#1a75c9" stroke-width="2"><rect x="18" y="18" width="16" height="16"/><rect x="4" y="4" width="10" height="10"/><rect x="38" y="4" width="10" height="10"/><rect x="4" y="38" width="10" height="10"/><rect x="38" y="38" width="10" height="10"/><path d="M14 9H26V18M38 9H30M9 14V30H18M34 26H43V38M26 34V43H14"/></svg></div>
    <h3>Integrated</h3><p>Integrated into MD clinical<br>workflows and IT systems</p>
  </div>
  <div class="feature" style="left:339px">
    <div class="icon"><svg width="52" height="52" viewBox="0 0 52 52" fill="none" stroke="#1a75c9" stroke-width="2"><path d="M12 46V34Q4 28 6 18Q10 4 26 4Q44 6 44 22L48 30H44V38H36V46"/><rect x="18" y="14" width="16" height="16"/><path d="M22 10V14M30 10V14M22 30V34M30 30V34M14 18H18M14 26H18M34 18H38M34 26H38"/></svg></div>
    <h3>Automated PA</h3><p>Automated PA removing manual processes, saving administrative costs</p>
  </div>
  <div class="feature" style="left:602px">
    <div class="icon"><svg width="52" height="52" viewBox="0 0 52 52" fill="none" stroke="#1a75c9" stroke-width="2"><rect x="8" y="6" width="36" height="30" rx="2"/><path d="M2 42H50L46 36H6Z"/><path d="M16 30V22H20V30M22 30V18Q22 14 26 14V20H32Q34 22 32 30Z"/><path d="M34 12L36 8L38 12L42 12L39 15L40 19L36 17L32 19L33 15L30 12Z"/></svg></div>
    <h3>Improved care quality</h3><p>Improved care quality equal or<br>better personalized care</p>
  </div>
  <div class="feature" style="left:863px">
    <div class="icon"><svg width="52" height="52" viewBox="0 0 52 52" fill="none" stroke="#1a75c9" stroke-width="2"><rect x="14" y="4" width="30" height="40"/><path d="M20 12H38M20 18H38M20 24H30"/><circle cx="12" cy="20" r="8"/><path d="M12 16V24"/><rect x="4" y="30" width="16" height="18"/><path d="M8 35H16M8 40H16M8 44H16"/><path d="M34 40L46 26L50 30L38 44L33 45Z"/></svg></div>
    <h3>Financial gains</h3><p>Financial gains through reduced<br>write-offs and right-sized care</p>
  </div>
</section>

<section class="evidence">
  <h2 class="abs section-title" style="top:1872px">CLINICAL <span>EVIDENCE</span></h2>
  <article class="card" style="left:110px">
    <div class="thumb" role="img" aria-label="Photo of a doctor holding a phone with AI health graphics"></div>
    <h4>AI power saves time and improves treatment plan quality</h4>
    <div class="meta">&#9635; Dec 10, 2020 &nbsp;|&nbsp; &#9679; Alex Moran</div>
    <div class="rule"></div>
    <div class="dl"><svg width="12" height="14" viewBox="0 0 12 14" fill="none" stroke="#1a75c9" stroke-width="1.4"><path d="M1 1H8L11 4V13H1Z"/></svg>DownLoad Now</div>
  </article>
  <article class="card" style="left:443px">
    <div class="thumb" role="img" aria-label="Photo of a clinician reviewing records with digital scans"></div>
    <h4>Leveraging Artificial Intelligence (AI) clinical decision support</h4>
    <div class="meta">&#9635; Dec 10, 2020 &nbsp;|&nbsp; &#9679; Alex Moran</div>
    <div class="rule"></div>
    <div class="dl"><svg width="12" height="14" viewBox="0 0 12 14" fill="none" stroke="#1a75c9" stroke-width="1.4"><path d="M1 1H8L11 4V13H1Z"/></svg>DownLoad Now</div>
  </article>
  <article class="card" style="left:775px">
    <div class="thumb" role="img" aria-label="Photo of surgeons in an operating room with digital displays"></div>
    <h4>Implementation and impact of AI decision support software</h4>
    <div class="meta">&#9635; Dec 10, 2020 &nbsp;|&nbsp; &#9679; Alex Moran</div>
    <div class="rule"></div>
    <div class="dl"><svg width="12" height="14" viewBox="0 0 12 14" fill="none" stroke="#1a75c9" stroke-width="1.4"><path d="M1 1H8L11 4V13H1Z"/></svg>DownLoad Now</div>
  </article>
  <div class="abs scroll"><i></i></div>
</section>

<section class="partners">
  <h2 class="abs section-title" style="top:2519px">OUR <span>PARTNERS</span></h2>
  <div class="partner" style="left:110px">Bayridge Health</div>
  <div class="partner" style="left:357px">Hollins Health System</div>
  <div class="partner" style="left:604px">Northgate Medicine</div>
  <div class="partner" style="left:850px">Eastlake Cancer Center</div>
</section>

<footer>
  <div class="abs brand" style="left:116px;top:2900px;font-size:38px"><span>Talvora Health</span><span class="dot" style="background:#fff"></span></div>
  <span class="social" style="left:130px" role="img" aria-label="Social link"></span>
  <span class="social" style="left:179px" role="img" aria-label="Social link"></span>
  <span class="social" style="left:227px" role="img" aria-label="Social link"></span>
  <span class="social" style="left:276px" role="img" aria-label="Social link"></span>
  <div class="abs footer-col" style="left:588px;top:2880px">
    <h5>Company</h5>
    <a>Home</a><a>Solutions</a><a>Clinical Evidence</a><a>About</a><a>Contact Us</a>
  </div>
  <div class="abs footer-col" style="left:928px;top:2880px">
    <h5>Information</h5>
    <a>Terms &amp; Condition</a><a>Privacy Policy</a><a>Disclaimer</a><a>Site Map</a><a>Customer Support</a>
  </div>
  <p class="abs copy">2020 Copyright - Talvora-health &nbsp;| All Rights Reserved</p>
</footer>
</body>
</html>
```